Test and Tag business card design

We are an appliance test and tag company in Brisbane Australia requiring a business card design.
I don't have a logo.
Card front: Matte black background with white font.
Card back: White background with black font colour
Examples are attached
Minimalist design
Reason: Looking for more designs with an extreme minimal feel
Industry/Entity Type
Appliance
Contact Information for Business Card
Business name: Harbor Check and Label
Description: Onsite Electrical Testing and Tagging
Licence No. 41853
Name: Greg Pellow
Mobile: 0418 526 937
Email: greg@harborcheckandlabel.com.au
Web: harborcheckandlabel.com.au
Logo Text
Harbor Check and Label
Look and feel

```html
<!DOCTYPE html>
<html lang="en">
<head>
<meta charset="utf-8">
<title>Harbor Check and Label – Business Card</title>
<link rel="stylesheet" href="https://fonts.googleapis.com/css2?family=Cabin:wght@400;600;700&display=swap">
<style>
  :root {
    --page-bg: #ececec;
    --card-black: #141414;
    --card-black-soft: #1c1c1c;
    --text-white: #ffffff;
    --card-shadow: rgba(0, 0, 0, 0.28);
  }
  * { margin: 0; padding: 0; box-sizing: border-box; }
  html, body {
    width: 1200px;
    height: 1000px;
    overflow: hidden;
    background: var(--page-bg);
    font-family: "Cabin", Arial, sans-serif;
  }
  .canvas {
    position: relative;
    width: 1200px;
    height: 1000px;
  }
  .business-card {
    position: absolute;
    left: 141px;
    top: 236px;
    width: 917px;
    height: 528px;
    background: linear-gradient(90deg, var(--card-black) 0%, var(--card-black) 42%, var(--card-black-soft) 100%);
    box-shadow: 4px 5px 6px var(--card-shadow);
    color: var(--text-white);
  }
  .licence {
    position: absolute;
    left: 59px;
    top: 45px;
    font-size: 19px;
    font-weight: 400;
  }
  .brand-mark {
    position: absolute;
    left: 60px;
    top: 254px;
    width: 260px;
    display: flex;
    align-items: center;
    gap: 10px;
  }
  .brand-mark__square {
    flex: 0 0 18px;
    width: 18px;
    height: 18px;
    background: var(--text-white);
  }
  .brand-mark__name {
    font-size: 20px;
    font-weight: 700;
    line-height: 1.2;
  }
  .company {
    position: absolute;
    left: 370px;
    top: 144px;
    font-size: 29px;
    font-weight: 700;
    line-height: 35px;
  }
  .company__name {
    font-size: 29px;
    font-weight: 700;
    text-transform: uppercase;
  }
  .company__tagline { letter-spacing: 0.3px; }
  .contact {
    position: absolute;
    left: 370px;
    top: 338px;
  }
  .contact__person {
    font-size: 25px;
    font-weight: 700;
    margin-bottom: 12px;
  }
  .contact__list { list-style: none; }
  .contact__item {
    display: flex;
    align-items: center;
    gap: 11px;
    height: 36px;
    font-size: 22px;
    font-weight: 400;
  }
  .contact__icon {
    width: 23px;
    height: 23px;
    flex: 0 0 23px;
  }
</style>
</head>
<body>
<main class="canvas">
  <section class="business-card" aria-label="Harbor Check and Label business card">
    <p class="licence">Licence No. 41853</p>

    <div class="brand-mark">
      <span class="brand-mark__square" aria-hidden="true"></span>
      <span class="brand-mark__name">Harbor Check and Label</span>
    </div>

    <header class="company">
      <h1 class="company__name">Harbor Check and Label</h1>
      <p class="company__tagline">Onsite Electrical Testing and Tagging</p>
    </header>

    <div class="contact">
      <p class="contact__person">Greg Pellow</p>
      <ul class="contact__list">
        <li class="contact__item">
          <svg class="contact__icon" viewBox="0 0 24 24" aria-hidden="true">
            <rect x="1" y="1" width="22" height="22" rx="4" fill="var(--text-white)"/>
            <path d="M8 5c-1.5 1-2.5 3-2.5 5.5 0 4 3 8 6.5 8.5l1.5-3-2-1.2c-1.2-1-1.8-3-1.3-4.6L12.5 9 11 5.5z" fill="var(--card-black)"/>
          </svg>
          <span>0418 526 937</span>
        </li>
        <li class="contact__item">
          <svg class="contact__icon" viewBox="0 0 24 24" aria-hidden="true">
            <rect x="1" y="4" width="22" height="16" rx="3" fill="var(--text-white)"/>
            <path d="M4 7l8 6 8-6" fill="none" stroke="var(--card-black)" stroke-width="2"/>
          </svg>
          <span>greg@harborcheckandlabel.com.au</span>
        </li>
        <li class="contact__item">
          <svg class="contact__icon" viewBox="0 0 24 24" aria-hidden="true">
            <circle cx="12" cy="12" r="11" fill="var(--text-white)"/>
            <g fill="none" stroke="var(--card-black)" stroke-width="1.6">
              <ellipse cx="12" cy="12" rx="4.5" ry="9"/>
              <path d="M3 12h18M5 7h14M5 17h14"/>
            </g>
          </svg>
          <span>www.harborcheckandlabel.com.au</span>
        </li>
      </ul>
    </div>
  </section>
</main>
</body>
</html>
```